MOLT - Monitoring Natural Hazards from Space Web Application

KORVEN Sarl is a Luxembourg based Space-Startup that works in the field of Earth Observation. KORVEN is a platform able to extract value-added information from satellite data and is specialized in mapping Natural Disaster (floods, fires etc).

We are now developing a new vertical tool, called MOLT, dedicated to the monitoring of natural hazards in Humanitarian Camps around the world.

The goal of MOLT is to hide to the users' all the complexity of the Satellite Image processing and just provide them the results.

This project require to Design 4 pages of MOLT:
• Public Home Page (Code - V01)
• Dashboard (private Home Page) (Code - V03)
• Monitor (web GIS) (Code - V14)
• Registration Page (Code - V04)

We would like to provide the required time to make a good job.

Target Market(s)

Humanitarian Agencies, Goverments

Coding

Coded - Design and coding required

Number of Pages Required

4 page

Font styles to use
Other font styles liked:
• see the manual attached

Requirements
Must have
• 4 pages. One Home, one form, one dashboard and one web map.
Nice to have
• Please read the attachment with all the detailed instructions

```html
<!DOCTYPE html>
<html lang="en">
<head>
<meta charset="utf-8">
<title>MOLT – Create account</title>
<link href="https://fonts.googleapis.com/css2?family=Instrument+Sans:wght@400;500&family=Space+Mono:wght@700&display=swap" rel="stylesheet">
<style>
  :root {
    --teal-dark: #2a4c5a;
    --band: #d2e9ef;
    --ink: #262626;
    --ink-soft: #8a8a8a;
    --placeholder: #555b5e;
    --field-border: #1f2a30;
    --focus-ring: #a9c1c9;
    --white: #ffffff;
    --accent: #d9a62b;
  }
  * { box-sizing: border-box; margin: 0; padding: 0; }
  html, body { width: 1154px; height: 1200px; overflow: hidden; background: var(--white); }
  body { font-family: "Instrument Sans", Arial, sans-serif; color: var(--ink); position: relative; }

  .topbar { height: 47px; background: var(--teal-dark); display: flex; align-items: center; padding-left: 19px; gap: 7px; }
  .brand-dot { width: 22px; height: 22px; border-radius: 50%; border: 2px solid var(--accent); }
  .brand-name { font-size: 14px; font-weight: 500; color: var(--accent); letter-spacing: .5px; }

  .hero { height: 110px; background: var(--band); text-align: center; padding-top: 28px; }
  .hero-title { font-family: "Space Mono", monospace; font-weight: 700; font-size: 26px; line-height: 32px; color: #333; }
  .hero-sub { margin-top: 4px; font-size: 12px; color: var(--ink-soft); }
  .hero-sub a { color: var(--ink); text-decoration: underline; text-underline-offset: 2px; }

  .form { position: absolute; left: 324px; top: 191px; width: 504px; }
  .section-title { font-family: "Space Mono", monospace; font-weight: 700; font-size: 19px; line-height: 20px; color: #333; }
  .section-sub { margin-top: 7px; font-size: 12px; line-height: 16px; color: #9a9a9a; }
  .section-org { margin-top: 37px; }

  .fields { margin-top: 20px; display: grid; grid-template-columns: 244px 244px; column-gap: 16px; row-gap: 24.4px; }
  .field { height: 62px; }
  .field.wide { grid-column: 1 / 3; }
  .field-label { display: block; font-size: 12px; line-height: 16px; margin-bottom: 8px; color: var(--ink); }
  .field-label em { color: #777; font-style: italic; }
  .input { height: 38px; border: 1px solid var(--field-border); border-radius: 2px; display: flex; align-items: center; padding: 0 13px; font-size: 11px; color: var(--placeholder); gap: 8px; }
  .input .value { color: var(--ink); font-size: 12px; }
  .input .text { flex: 1; }
  .input.focused { border-color: var(--teal-dark); box-shadow: 0 0 0 3px var(--focus-ring); }
  .caret { width: 1px; height: 13px; background: var(--ink); flex: 1; max-width: 1px; margin-right: auto; }
  .show { display: flex; align-items: center; gap: 6px; color: #777; font-size: 11.5px; }
  .phone-flag { display: flex; align-items: center; gap: 9px; margin-right: 4px; }

  .checks { margin-top: 24px; }
  .check { display: flex; align-items: center; gap: 9px; font-size: 12.5px; height: 18px; }
  .check + .check { margin-top: 14px; }
  .check-box { width: 18px; height: 18px; border-radius: 2px; background: var(--teal-dark); display: flex; align-items: center; justify-content: center; }
  .check a { color: var(--ink); text-decoration: underline; text-underline-offset: 2px; }

  .submit { margin-top: 23px; width: 504px; height: 38px; background: var(--teal-dark); color: var(--white); border: none; border-radius: 2px; font-family: inherit; font-size: 14px; font-weight: 500; }
</style>
</head>
<body>
  <header class="topbar">
    <span class="brand-dot"></span>
    <span class="brand-name">MOLT</span>
  </header>

  <section class="hero">
    <h1 class="hero-title">Sign in</h1>
    <p class="hero-sub">Dont have an account? <a href="#">Sign up</a></p>
  </section>

  <form class="form">
    <h2 class="section-title">Basic Info</h2>
    <p class="section-sub">Please enter basic information to create account</p>
    <div class="fields">
      <div class="field"><label class="field-label">Full Name</label><div class="input"><span class="value">Jane Doe</span></div></div>
      <div class="field"><label class="field-label">Email</label><div class="input"><span class="value">janedoe@korvenmail.io</span></div></div>
      <div class="field"><label class="field-label">Password</label>
        <div class="input focused"><span class="caret"></span>
          <span class="show"><svg width="12" height="9" viewBox="0 0 12 9"><path d="M1 4.5C2.5 1.8 4 1 6 1s3.5.8 5 3.5C9.5 7.2 8 8 6 8S2.5 7.2 1 4.5z" fill="none" stroke="#777"/><circle cx="6" cy="4.5" r="1.5" fill="none" stroke="#777"/></svg>Show</span></div></div>
      <div class="field"><label class="field-label">Password</label>
        <div class="input"><span class="text">Confirm Password</span>
          <span class="show"><svg width="12" height="9" viewBox="0 0 12 9"><path d="M1 4.5C2.5 1.8 4 1 6 1s3.5.8 5 3.5C9.5 7.2 8 8 6 8S2.5 7.2 1 4.5z" fill="none" stroke="#777"/><circle cx="6" cy="4.5" r="1.5" fill="none" stroke="#777"/></svg>Show</span></div></div>
      <div class="field"><label class="field-label">Email address</label>
        <div class="input"><span class="text">Enter email</span><svg width="15" height="11" viewBox="0 0 15 11"><rect x=".5" y=".5" width="14" height="10" fill="none" stroke="#777"/><path d="M.5.5l7 5.5 7-5.5M.5 10.5l5.5-5M14.5 10.5l-5.5-5" fill="none" stroke="#777"/></svg></div></div>
      <div class="field"><label class="field-label">Confirm Email address</label>
        <div class="input"><span class="text">Enter email</span><svg width="15" height="11" viewBox="0 0 15 11"><rect x=".5" y=".5" width="14" height="10" fill="none" stroke="#777"/><path d="M.5.5l7 5.5 7-5.5M.5 10.5l5.5-5M14.5 10.5l-5.5-5" fill="none" stroke="#777"/></svg></div></div>
      <div class="field"><label class="field-label">Mobile No.</label>
        <div class="input"><span class="phone-flag"><svg width="16" height="11" viewBox="0 0 16 11"><rect width="16" height="11" fill="#fff"/><path d="M0 .8h16M0 2.5h16M0 4.2h16M0 5.9h16M0 7.6h16M0 9.3h16" stroke="#d2374a" stroke-width=".9"/><rect width="7" height="5.9" fill="#3b4a9c"/></svg><svg width="8" height="5" viewBox="0 0 8 5"><path d="M0 0h8L4 5z" fill="#1f2a30"/></svg></span><span class="text">Enter Mobile no.</span></div></div>
    </div>

    <h2 class="section-title section-org">Organization Info</h2>
    <p class="section-sub">Please enter basic information to create account</p>
    <div class="fields">
      <div class="field"><label class="field-label">Organization name</label><div class="input"><span class="text">Enter organization name</span></div></div>
      <div class="field"><label class="field-label">Organization type</label>
        <div class="input"><span class="text">Select type</span><svg width="9" height="6" viewBox="0 0 9 6"><path d="M1 1l3.5 3.5L8 1" fill="none" stroke="#1f2a30" stroke-width="1.4"/></svg></div></div>
      <div class="field wide"><label class="field-label">Address 1</label><div class="input"><span class="text">Enter email</span></div></div>
      <div class="field"><label class="field-label">City</label>
        <div class="input"><span class="text">Select city</span><svg width="9" height="6" viewBox="0 0 9 6"><path d="M1 1l3.5 3.5L8 1" fill="none" stroke="#1f2a30" stroke-width="1.4"/></svg></div></div>
      <div class="field"><label class="field-label">Country</label>
        <div class="input"><span class="text">Select Country</span><svg width="9" height="6" viewBox="0 0 9 6"><path d="M1 1l3.5 3.5L8 1" fill="none" stroke="#1f2a30" stroke-width="1.4"/></svg></div></div>
      <div class="field"><label class="field-label">Postal code</label><div class="input"><span class="text">Enter Postal code</span></div></div>
      <div class="field"><label class="field-label">Telephone No. <em>(Optional)</em></label><div class="input"><span class="text">Enter Telephone no.</span></div></div>
    </div>

    <div class="checks">
      <div class="check"><span class="check-box"><svg width="11" height="8" viewBox="0 0 11 8"><path d="M1 4l3 3 6-6" fill="none" stroke="#fff" stroke-width="1.4"/></svg></span>Confirm Terms And Conditions of MOLT. <a href="#">Read</a></div>
      <div class="check"><span class="check-box"><svg width="11" height="8" viewBox="0 0 11 8"><path d="M1 4l3 3 6-6" fill="none" stroke="#fff" stroke-width="1.4"/></svg></span>Confirm Privacy Polciy of MOLT. <a href="#">Read</a></div>
    </div>

    <button type="button" class="submit">Create account</button>
  </form>
</body>
</html>
```